Business Card Design for Law firm - already have logo

Now that we have a logo, we need a business card design - our logo is attached -it is salaryman font if that helps - we would like a file that can be uploaded to kellumo (www.kellumo.com) using the logo and with the following information on it:
Dunmore Law Firm, P.C.
Felix Dunmore, Esq.
6718 NE 19th Ave.
Portland, OR 97284
971.555.0142 phone
971.555.0187 fax
fel@dunmore.net
Skype: feldunmore
Google talk: felix.dunmore@quillmail.com
Target Market(s)
our business cards are distributed to corporate executives, technology professionals and healthcare providers
Industry/Entity Type
Business
Look and feel

```html
<!DOCTYPE html>
<html lang="en">
<head>
<meta charset="utf-8">
<title>Dunmore Law Firm – Business Card</title>
<link href="https://fonts.googleapis.com/css2?family=Open+Sans:wght@400;600;700&display=swap" rel="stylesheet">
<style>
  :root {
    --backdrop: #e9e6e2;
    --card-white: #ffffff;
    --ink: #3a3a3a;
    --icon: #5a5a5a;
    --name: #ffffff;
    --space-deep: #1c1626;
    --space-mid: #5a2d4e;
    --space-pink: #c4718f;
    --space-glow: #e7a9c0;
  }
  * { margin: 0; padding: 0; box-sizing: border-box; }
  html, body {
    width: 1200px; height: 646px; overflow: hidden;
    background: var(--backdrop);
    font-family: "Open Sans", Arial, sans-serif;
  }
  .card {
    position: absolute; left: 100px; top: 38px;
    width: 1000px; height: 570px;
    overflow: hidden;
    box-shadow: 0 6px 24px rgba(0,0,0,0.18);
  }
  .card-art { position: absolute; inset: 0; width: 100%; height: 100%; }
  .brand {
    position: absolute; left: 70px; top: 250px;
  }
  .brand-name {
    font-size: 58px; font-weight: 400; letter-spacing: 10px;
    color: var(--ink); line-height: 1;
  }
  .brand-firm {
    margin-top: 8px; margin-left: 150px;
    font-size: 17px; color: var(--ink);
  }
  .contact-list {
    position: absolute; left: 560px; top: 96px;
    list-style: none;
  }
  .contact-list li {
    display: flex; align-items: flex-start; gap: 14px;
    font-size: 20px; line-height: 27px; color: var(--ink);
    margin-bottom: 4px;
  }
  .contact-list svg { flex: 0 0 24px; width: 24px; height: 24px; margin-top: 2px; fill: var(--icon); }
  .holder-name {
    position: absolute; left: 120px; top: 470px;
    font-size: 30px; font-weight: 700; color: var(--name);
  }
  .holder-name span { font-size: 22px; font-weight: 600; }
</style>
</head>
<body>
<div class="card">
  <svg class="card-art" viewBox="0 0 1000 570" preserveAspectRatio="none">
    <defs>
      <radialGradient id="space-glow" cx="0.78" cy="0.55" r="0.6">
        <stop offset="0" stop-color="var(--space-glow)"/>
        <stop offset="0.35" stop-color="var(--space-pink)"/>
        <stop offset="0.75" stop-color="var(--space-mid)"/>
        <stop offset="1" stop-color="var(--space-deep)"/>
      </radialGradient>
    </defs>
    <rect role="img" aria-label="Pink and violet nebula photograph" width="1000" height="570" fill="url(#space-glow)"/>
    <path class="card-panel" fill="var(--card-white)"
      d="M0,0 H560 C700,0 820,60 1000,38 V262 C840,300 700,330 560,362 C380,402 200,385 0,440 Z"/>
  </svg>

  <div class="brand">
    <div class="brand-name">DUNMORE</div>
    <div class="brand-firm">Dunmore Law Firm, P.C.</div>
  </div>

  <ul class="contact-list">
    <li><svg viewBox="0 0 24 24"><path d="M12 2a7 7 0 0 0-7 7c0 5 7 13 7 13s7-8 7-13a7 7 0 0 0-7-7zm0 9.5A2.5 2.5 0 1 1 12 6.5a2.5 2.5 0 0 1 0 5z"/></svg><span>6718 NE 19th Ave.<br>Portland, OR 97284</span></li>
    <li><svg viewBox="0 0 24 24"><path d="M6.6 10.8a15 15 0 0 0 6.6 6.6l2.2-2.2a1 1 0 0 1 1-.25 11 11 0 0 0 3.6.6 1 1 0 0 1 1 1V20a1 1 0 0 1-1 1A17 17 0 0 1 3 4a1 1 0 0 1 1-1h3.5a1 1 0 0 1 1 1 11 11 0 0 0 .6 3.6 1 1 0 0 1-.25 1z"/></svg><span>971.555.0142</span></li>
    <li><svg viewBox="0 0 24 24"><path d="M6 3h12v5H6zM4 9h16a2 2 0 0 1 2 2v6h-4v4H6v-4H2v-6a2 2 0 0 1 2-2zm4 7v3h8v-3z"/></svg><span>971.555.0187</span></li>
    <li><svg viewBox="0 0 24 24"><path d="M3 5h18v14H3zm2 2v.5l7 5 7-5V7zm0 3v7h14v-7l-7 5z"/></svg><span>fel@dunmore.net</span></li>
    <li><svg viewBox="0 0 24 24"><circle cx="12" cy="12" r="9"/></svg><span>feldunmore</span></li>
    <li><svg viewBox="0 0 24 24"><path d="M12 3c5 0 9 3.4 9 7.5S17 18 12 18c-.9 0-1.8-.1-2.6-.3L4 21l1.4-4.3C4 15.4 3 13 3 10.5 3 6.4 7 3 12 3z"/></svg><span>felix.dunmore@quillmail.com</span></li>
  </ul>

  <div class="holder-name">Felix Dunmore, <span>Esq.</span></div>
</div>
</body>
</html>
```